Norvale Email Signature Banners – Fabrication Capability Series

www.Norvale.com.au is an Australian engineering and fabrication company specialising in fabrication and welding of :
steel piping spools,
skids and frames,
small volume process steel tanks
and general steel fabrication
We require four distinct banner designs for use in Teldrin Quillmark email signatures. Each banner will highlight a specific capability while maintaining a consistent brand identity.
Deliverables
Four banners total:
Piping Spools Fabrication – focus on precision welding and stainless steel pipework
Skid & Frames Fabrication – highlight skid systems and structural frames
Small Steel Tanks Fabrication – show fabricated tanks and workshop craftsmanship
General Fabrication Solutions – broad steel fabrication theme for company-wide use
Dimensions: 600–700 px wide × 100 px high
Format: PNG (preferred), small file size prefered
Resolution: 72 dpi
Background: non-transparent, industrial or workshop setting
Text examples:
1. Piping Spools Fabrication
Option A: “Expert Fabrication Solutions for Process Piping”
Option B: “Precision Welding for Complex Systems”
Option C: “Delivering Quality in Every Spool”
Option D: “Engineered for Flow, Built for Strength”
2. Skid & Frames Fabrication
Option A: “Custom Engineered Modular Systems”
Option B: “Built Strong. Designed Smart.”
Option C: “Reliable Frames for Industrial Performance”
Option D: “Modular Fabrication for Seamless Integration”
3. Small Steel Tanks Fabrication
Option A: “Precision Built for Your Needs”
Option B: “Compact Strength. Proven Durability.”
Option C: “Fabricated for Performance and Longevity”
Option D: “Small Tanks. Big Reliability.”
4. General Fabrication Solutions
Option A: “Quality Craftsmanship, Proven Results”
Option B: “Your Partner in Precision Fabrication”
Option C: “Engineering Excellence in Every Weld”
Option D: “Australian Fabrication. Global Standards.”
Style Direction
Clean, professional, and engineering‑focused
Use Norvale brand colours
Blend photo realism with vector clarity (no heavy gradients)
Include subtle industrial textures or workshop imagery
Typography: bold sans‑serif, legible at small scale
Usage Context
These banners will appear at the bottom of staff email signatures via Quillmark Email Signature Tool for Teldrin 365, so clarity and fast loading are essential. No Logo is required in the banners.
Reference
Existing Norvale signature is attached. Colour palette to match the signature style and logo.
Target Market(s)
Engineering and construction companies,
Industry/Entity Type
Engineering fabrication design

```html
<!DOCTYPE html>
<html lang="en">
<head>
<meta charset="UTF-8">
<title>Norvale – Small Steel Tanks Fabrication Banner</title>
<link rel="stylesheet" href="https://fonts.googleapis.com/css2?family=Exo+2:wght@700&display=swap">
<style>
  :root {
    --page-bg: #e6e7e9;
    --banner-white: #f4f5f6;
    --brand-blue: #1d8fd0;
    --brand-grey: #6b6e72;
    --rule-grey: #8d9094;
    --steel-light: #d3d6d9;
    --steel-mid: #a4a9af;
    --steel-dark: #7c838b;
    --shop-navy: #5d6b80;
  }
  * { margin: 0; padding: 0; box-sizing: border-box; }
  html, body {
    width: 1200px;
    height: 1200px;
    overflow: hidden;
    background: var(--page-bg);
  }
  .canvas {
    position: relative;
    width: 1200px;
    height: 1200px;
  }
  .banner {
    position: absolute;
    left: 49px;
    top: 449px;
    width: 1102px;
    height: 302px;
    background: var(--banner-white);
    overflow: hidden;
  }
  .photo {
    position: absolute;
    top: 0;
    height: 100%;
  }
  .photo--tanks {
    left: 0;
    width: 42%;
    background: linear-gradient(90deg, var(--steel-dark) 0%, var(--steel-mid) 45%, var(--steel-light) 75%, var(--banner-white) 100%);
  }
  .photo--workshop {
    right: 0;
    width: 44%;
    background: linear-gradient(270deg, var(--shop-navy) 0%, var(--steel-dark) 25%, var(--steel-mid) 55%, var(--steel-light) 80%, var(--banner-white) 100%);
  }
  .rules {
    position: absolute;
    inset: 0;
    width: 100%;
    height: 100%;
  }
  .tagline {
    position: absolute;
    left: 0;
    right: 0;
    top: 88px;
    text-align: center;
    font-family: "Exo 2", sans-serif;
    font-weight: 700;
    font-size: 55px;
    line-height: 63px;
    letter-spacing: 1px;
    color: var(--brand-grey);
  }
  .tagline__accent { color: var(--brand-blue); }
</style>
</head>
<body>
  <main class="canvas">
    <section class="banner" aria-label="Small steel tanks fabrication banner">
      <div class="photo photo--tanks" role="img" aria-label="Polished stainless steel tanks on a workbench with welding sparks behind"></div>
      <div class="photo photo--workshop" role="img" aria-label="Fabricator grinding a small stainless steel tank in a workshop"></div>

      <svg class="rules" viewBox="0 0 1102 302" preserveAspectRatio="none" aria-hidden="true">
        <line x1="0" y1="15" x2="738" y2="15" stroke="var(--brand-blue)" stroke-width="4"/>
        <line x1="0" y1="28" x2="664" y2="28" stroke="var(--rule-grey)" stroke-width="4"/>
        <line x1="434" y1="273" x2="1102" y2="273" stroke="var(--rule-grey)" stroke-width="4"/>
        <line x1="360" y1="288" x2="1102" y2="288" stroke="var(--brand-blue)" stroke-width="4"/>
      </svg>

      <h1 class="tagline">
        <span class="tagline__accent">Compact</span> Strength.<br>
        Proven <span class="tagline__accent">Durability.</span>
      </h1>
    </section>
  </main>
</body>
</html>
```